Personal website: Intro to a software engineer, filmmaker, entrepreneur

I'm looking to do a redesign of my website. It's had many forms over the years, primarily because it's been hard to pin down all what I want to communicate. I'm a software engineer, filmmaker, writer, and entrepreneur. I'm looking to showcase not only what I've done and what I can do, but also who I am, what I'm interested in, and what I have to say. The minimal content at this point would be: Name, photo of me, short intro, publications on Tarnly (title, description, date), and social links. In the future I could see adding notable projects, open source contributions, and possibly skills. Think of it as an intro to Dane Colpitt.

I would like this to be all on one page. If I were to pin down the design atheistic I'm going for it would be: Warm, sophisticated, simple, clear, minimal, creative, flat, thoughtful, artistic, and soft. I imagine typography taking more over a role here than images. I know a lot of design is image focused, but I'd rather any photos be accents than main content.

I'm more than happy to give more details if more is needed/wanted.
Updates

Designs look the same

Target Market(s)

Fellow co-creators

Number of Pages Required

1 page

Requirements
Must have
• Name, photo of me, short intro, publications on Tarnly (title, description, date), and social links.
Nice to have
• Notable projects, open source contributions, and skills
Should not have
• It should not be overly techy. I'm about building solutions and sharing ideas.
• Should not look corporate.

```html
<!DOCTYPE html>
<html lang="en">
<head>
<meta charset="utf-8">
<title>Dane Colpitt</title>
<link rel="stylesheet" href="https://fonts.googleapis.com/css2?family=Poppins:wght@400;500;600;700&family=Dancing+Script:wght@600&display=swap">
<style>
:root{
  --orange:#f79a45;
  --ink:#111111;
  --white:#ffffff;
  --footer:#4f4d4d;
  --card:#8f8f8f;
  --text-soft:#fff3e6;
  --hero-top:#b79a6a;
  --hero-mid:#e3a64a;
  --hero-low:#d98d33;
}
*{box-sizing:border-box;margin:0;padding:0}
html,body{width:737px;height:1200px;overflow:hidden;background:var(--white)}
body{position:relative;font-family:"Poppins",sans-serif;color:var(--ink)}
.abs{position:absolute}

/* hero */
.hero{left:0;top:0;width:737px;height:320px;overflow:hidden}
.hero-bg{position:absolute;inset:0;
  background:linear-gradient(180deg,var(--hero-top) 0,var(--hero-mid) 55%,var(--hero-low) 100%)}
.brand{left:24px;top:14px;font-family:"Dancing Script",cursive;font-size:29px;color:var(--white);font-weight:600}
.contact{right:14px;top:20px;display:flex;align-items:center;font-size:10.5px;color:var(--white)}
.contact svg{display:block}
.contact .item{display:flex;align-items:center;gap:6px;margin-left:12px}
.avatar{left:322px;top:94px;width:88px;height:88px;border-radius:50%;border:3px solid var(--white);
  background:linear-gradient(180deg,#c79b78 0,#8a5d3f 55%,#23262c 100%)}
.name-box{left:292px;top:189px;width:136px;height:57px;border:1px solid rgba(255,255,255,.8);border-right:none;text-align:center;color:var(--white);padding-top:5px}
.name-box h1{font-size:15px;font-weight:700;letter-spacing:2.6px;line-height:18px;white-space:nowrap}
.name-box p{font-size:8.6px;line-height:11.5px;margin-top:3px}

/* about */
.about-photo{left:135px;top:350px;width:177px;height:185px;
  background:linear-gradient(90deg,#7a4b2a 0,#b0703c 40%,#2a2d35 50%,#2a2d35 62%,#b97a44 72%,#8b5631 100%)}
.about{left:350px;top:380px;width:262px}
.about h2{font-size:15px;font-weight:600;line-height:20px}
.about p{font-size:8.6px;line-height:11.8px;margin-top:3px}
.read-more{display:block;font-size:8.4px;font-weight:600;margin-top:6px}

/* posts grid */
.cell{width:246px;height:205px}
.post{background:var(--orange);color:var(--white);padding-left:56px;padding-top:52px}
.post .date{font-size:9px;line-height:12px}
.post h3{font-size:10px;font-weight:600;line-height:15px;margin-top:2px}
.post p{font-size:7.6px;line-height:10.7px;color:var(--text-soft);width:142px;margin-top:2px}
.post .more{font-size:6.3px;font-weight:700;margin-top:5px;display:block}
.photo-camera{background:linear-gradient(90deg,#6d6a66 0,#b9b7b2 35%,#f2f0ee 55%,#e8e6e4 80%,#cfcdc9 100%)}
.photo-desk{background:linear-gradient(160deg,#d8dcd5 0,#a88660 35%,#c9a27a 60%,#8a6a4a 100%)}
.photo-laptop{background:linear-gradient(135deg,#3a3f4a 0,#3f5aa6 40%,#8aa0d8 60%,#d2d2d2 85%,#b8b8b8 100%)}

/* footer */
.footer{left:0;top:976px;width:737px;height:224px;background:var(--footer);color:var(--white)}
.footer-brand{left:0;width:737px;top:14px;text-align:center;font-family:"Dancing Script",cursive;font-size:30px;font-weight:600}
.info{top:61px;width:177px;height:107px;background:var(--card);text-align:center;display:flex;flex-direction:column;align-items:center;justify-content:center}
.info h4{font-size:14.5px;font-weight:400;line-height:19px}
.info p{font-size:10px;line-height:14.5px}
.socials{display:flex;gap:10px;margin-top:6px}
.socials span{width:10px;height:10px;border-radius:50%;background:var(--white)}
.copyright{left:0;width:737px;top:188px;text-align:center;font-size:6.5px}
</style>
</head>
<body>

<header class="abs hero">
  <div class="hero-bg" role="img" aria-label="Warm sunset landscape photograph over water"></div>
  <div class="abs brand">Dane Colpitt</div>
  <div class="abs contact">
    <span class="item">
      <svg width="11" height="11" viewBox="0 0 24 24"><path fill="#fff" d="M6.6 10.8a15.1 15.1 0 0 0 6.6 6.6l2.2-2.2c.3-.3.7-.4 1-.2 1.1.4 2.3.6 3.6.6.6 0 1 .4 1 1V20c0 .6-.4 1-1 1A17 17 0 0 1 3 4c0-.6.4-1 1-1h3.5c.6 0 1 .4 1 1 0 1.3.2 2.5.6 3.6.1.3 0 .7-.2 1z"/></svg>
      555-204-7183
    </span>
    <span class="item">
      <svg width="12" height="9" viewBox="0 0 24 18"><rect x="1" y="1" width="22" height="16" fill="none" stroke="#fff" stroke-width="2"/><path d="M1 1l11 9 11-9" fill="none" stroke="#fff" stroke-width="2"/></svg>
      hello@colpittstudio.net
    </span>
  </div>
  <div class="abs avatar" role="img" aria-label="Portrait photo of Dane Colpitt"></div>
  <div class="abs name-box">
    <h1>Dane Colpitt</h1>
    <p>Software Engineer, Filmmaker,<br>Writer, &amp; Entrepreneur.</p>
  </div>
</header>

<section>
  <div class="abs about-photo" role="img" aria-label="Dane Colpitt in a suit leaning on a wooden wall"></div>
  <div class="abs about">
    <h2>About Me</h2>
    <p>Lorem ipsum dolor sit amet, consectetur adipiscing elit. Vivamus posuere quam non justo consectetur, ut semper eros tincidunt. Lorem ipsum dolor sit amet, consectetur adipiscing elit. Cras auctor mauris purus, sed dictum risus gravida eu. Nullam a vestibulum orci. Mauris ac velit luctus, feugiat nisl quis, dignissim odio. Ut non enim augue. In tempus pulvinar velit a consectetur.</p>
    <span class="read-more">Read More ›</span>
  </div>
</section>

<section>
  <article class="abs cell post" style="left:0;top:566px">
    <div class="date">05.09.2018</div>
    <h3>Lorem Ipsum is simply dummy.</h3>
    <p>Lorem ipsum dolor sit amet, consectetur adipiscing elit. Integer cursus condimentum aliquam. Nullam feugiat erat et eros eleifend tincidunt.</p>
    <span class="more">READ MORE ›</span>
  </article>
  <div class="abs cell photo-camera" style="left:246px;top:566px;width:245px" role="img" aria-label="Person in white trousers holding a camera"></div>
  <article class="abs cell post" style="left:491px;top:566px;padding-left:53px">
    <div class="date">05.09.2018</div>
    <h3>Lorem Ipsum is simply dummy.</h3>
    <p>Lorem ipsum dolor sit amet, consectetur adipiscing elit. Integer cursus condimentum aliquam. Nullam feugiat erat et eros eleifend tincidunt.</p>
    <span class="more">READ MORE ›</span>
  </article>

  <div class="abs cell photo-desk" style="left:0;top:771px" role="img" aria-label="Wooden desk with notebook, coffee and plant"></div>
  <article class="abs cell post" style="left:246px;top:771px;width:245px;padding-left:52px">
    <div class="date">05.09.2018</div>
    <h3>Lorem Ipsum is simply dummy.</h3>
    <p>Lorem ipsum dolor sit amet, consectetur adipiscing elit. Integer cursus condimentum aliquam. Nullam feugiat erat et eros eleifend tincidunt.</p>
    <span class="more">READ MORE ›</span>
  </article>
  <div class="abs cell photo-laptop" style="left:491px;top:771px" role="img" aria-label="Open laptop on a desk"></div>

  <svg class="abs" style="left:0;top:763px" width="737" height="16" viewBox="0 0 737 16">
    <polygon points="105,8 131,8 118,16" fill="var(--orange)"/>
    <polygon points="357,8 383,8 370,0" fill="var(--orange)"/>
    <polygon points="605,8 631,8 618,16" fill="var(--orange)"/>
  </svg>
</section>

<footer class="abs footer">
  <div class="abs footer-brand">Dane Colpitt</div>
  <div class="abs info" style="left:88px">
    <svg width="16" height="16" viewBox="0 0 24 24"><path fill="#fff" d="M6.6 10.8a15.1 15.1 0 0 0 6.6 6.6l2.2-2.2c.3-.3.7-.4 1-.2 1.1.4 2.3.6 3.6.6.6 0 1 .4 1 1V20c0 .6-.4 1-1 1A17 17 0 0 1 3 4c0-.6.4-1 1-1h3.5c.6 0 1 .4 1 1 0 1.3.2 2.5.6 3.6.1.3 0 .7-.2 1z"/></svg>
    <h4>Phone Number</h4>
    <p>555-204-7183</p>
  </div>
  <div class="abs info" style="left:279px">
    <svg width="14" height="19" viewBox="0 0 24 32"><path d="M12 2a9 9 0 0 0-9 9c0 7 9 18 9 18s9-11 9-18a9 9 0 0 0-9-9z" fill="none" stroke="#fff" stroke-width="2"/><circle cx="12" cy="11" r="3.5" fill="none" stroke="#fff" stroke-width="2"/></svg>
    <h4>Address</h4>
    <p>318 Alder Lane<br>Brookvale, WI 54010</p>
  </div>
  <div class="abs info" style="left:470px">
    <h4>Social Media</h4>
    <div class="socials"><span></span><span></span><span></span></div>
  </div>
  <div class="abs copyright">© 2018, Dane Colpitt.All Rights Reserved.</div>
</footer>

</body>
</html>
```